Training Consultant for Oil and Gas Drillers needs logo for business cards

I teach oil and gas professionals the skills required to keep rigs from blowing up. The company name is "Night Shift Pressure Guard", which is pronounced Night Shyft. Tour refers to the time on an oil rig when a worker is off for sleep and rest. I teach something called Well Control, which is how to maintain a pressure balance in the well so the hydro carbons don't come to surface unexpectedly( like the Cobalt Reach Platform).

Target Market(s)

Rig hands and oil companies

Contact Information for Business Card

Night Shift PG ( company name) with a new logo
My name (Derek Holloway )and Title (Well Control Consultant)
Phone number and address

Font styles to use
Serif
Sans Serif

Colors

Designer to choose colors to be used in the design.

Requirements
Must have
• I need a logo for the company. I do not have anything yet

```html
<!DOCTYPE html>
<html lang="en">
<head>
<meta charset="utf-8">
<title>Night Shift Pressure Guard – Business Card</title>
<link rel="stylesheet" href="https://fonts.googleapis.com/css2?family=Rubik:wght@700&family=Oswald:wght@500&family=Lato:ital,wght@0,400;1,400&display=swap">
<style>
  :root {
    --page: #eceae6;
    --card-white: #ffffff;
    --card-blue-top: #7cbbe6;
    --card-blue-bottom: #5fa6db;
    --brand-blue: #3b93d8;
    --name-blue: #3a9ad9;
    --rule-blue: #2f8ad4;
    --ink: #1c1c1c;
    --icon-blue: #4a9be0;
  }
  * { box-sizing: border-box; margin: 0; padding: 0; }
  html, body {
    width: 1200px; height: 1200px; overflow: hidden;
    background: var(--page);
  }
  .sheet {
    position: relative; width: 1200px; height: 1200px;
  }
  .card {
    position: absolute; left: 160px; width: 880px; height: 503px;
    border-radius: 4px;
    box-shadow: 0 6px 18px rgba(0,0,0,0.12);
  }
  .card--back {
    top: 70px;
    background: linear-gradient(160deg, var(--card-blue-top), var(--card-blue-bottom));
    display: flex; align-items: center; justify-content: center;
  }
  .card--front {
    top: 627px;
    background: var(--card-white);
  }
  .wordmark {
    display: flex; align-items: center; gap: 26px;
    font-family: "Rubik", sans-serif; font-weight: 700;
    letter-spacing: 1px; line-height: 1.05; text-transform: uppercase;
  }
  .wordmark__dot {
    width: 96px; height: 96px; border-radius: 50%; flex: none;
  }
  .card--back .wordmark { color: var(--card-white); font-size: 50px; }
  .card--back .wordmark__dot { background: var(--card-white); }
  .card--front .wordmark {
    position: absolute; left: 64px; top: 56px;
    color: var(--brand-blue); font-size: 44px; gap: 24px;
  }
  .card--front .wordmark__dot { background: var(--brand-blue); width: 88px; height: 88px; }
  .holder {
    position: absolute; left: 52px; top: 262px;
  }
  .holder__name {
    font-family: "Oswald", sans-serif; font-weight: 500;
    font-size: 40px; color: var(--name-blue); letter-spacing: 1px;
    text-transform: uppercase; line-height: 1;
  }
  .holder__title {
    font-family: "Lato", sans-serif; font-size: 19px; color: var(--ink);
    margin-top: 4px;
  }
  .rule {
    position: absolute; left: 48px; right: 110px; top: 348px;
    height: 2px; background: var(--rule-blue);
  }
  .contacts {
    position: absolute; left: 52px; top: 366px;
    list-style: none; font-family: "Lato", sans-serif; font-size: 18px;
    color: var(--ink); line-height: 1.35;
  }
  .contacts li { display: flex; align-items: center; gap: 10px; }
  .contacts svg { width: 13px; height: 13px; flex: none; }
  .address {
    position: absolute; right: 110px; top: 420px; text-align: right;
    font-family: "Lato", sans-serif; font-size: 20px; color: var(--ink);
    line-height: 1.25; font-style: normal;
  }
</style>
</head>
<body>
<main class="sheet">
  <section class="card card--back" aria-label="Card back">
    <div class="wordmark">
      <span class="wordmark__dot"></span>
      <span>Night Shift<br>Pressure Guard</span>
    </div>
  </section>

  <section class="card card--front" aria-label="Card front">
    <div class="wordmark">
      <span class="wordmark__dot"></span>
      <span>Night Shift<br>Pressure Guard</span>
    </div>

    <div class="holder">
      <p class="holder__name">Derek Holloway</p>
      <p class="holder__title">Well Control Consultant</p>
    </div>

    <div class="rule"></div>

    <ul class="contacts">
      <li>
        <svg viewBox="0 0 16 16" aria-hidden="true"><path fill="var(--icon-blue)" d="M3.5 1.5l2.5 0 1 3.5-1.8 1.2a8 8 0 0 0 4.6 4.6L11 9l3.5 1v2.5c0 1-1 2-2 2C6.5 14.5 1.5 9.5 1.5 3.5c0-1 1-2 2-2z"/></svg>
        5550-214-7788
      </li>
      <li>
        <svg viewBox="0 0 16 16" aria-hidden="true"><rect x="1" y="3" width="14" height="10" fill="var(--icon-blue)"/><path d="M1 3l7 6 7-6" fill="none" stroke="#fff" stroke-width="1.4"/></svg>
        derek@nightshiftpg.com
      </li>
      <li>
        <svg viewBox="0 0 16 16" aria-hidden="true"><circle cx="8" cy="8" r="6.5" fill="none" stroke="var(--icon-blue)" stroke-width="1.5"/><path d="M1.5 8h13M8 1.5c-3 3.5-3 9.5 0 13M8 1.5c3 3.5 3 9.5 0 13" fill="none" stroke="var(--icon-blue)" stroke-width="1.2"/></svg>
        www.nightshiftpg.com
      </li>
    </ul>

    <address class="address">
      Harbor Point Suite 12, Quay Road<br>
      Marlow Bay M4410, Brazil
    </address>
  </section>
</main>
</body>
</html>
```